Create the ONLY Supplement line for Male Entrepreneurs! (Verdant Crest MD)

I need a label designed for a new supplement brand that I am launching.

There are five products so need a design that I can simply change the wording for each individual product

The brand name is called verdant crest MD. The focus is male entrepreneurial health.

Target audience is men 35 to 55.

Concepts: the healthier you are in body the more money you will make in business.

Concept to copy: I want to make a clean minimalistic label mimicking Halvorsen MD (google it and you'll see what I mean)
Updates

Target Market(s)

male entrepreneurs 35-55

Industry/Entity Type

Health Supplement

Colors

Designer to choose colors to be used in the design.

Requirements
Must have
• Modern classy design, similar to Halvorsen MD.
Nice to have
• Highlight that the supplement is Doctor Approved.
Should not have
• No loud colors. Present it as high class.

```html
<!DOCTYPE html>
<html lang="en">
<head>
<meta charset="utf-8">
<title>Verdant Crest MD – Label System</title>
<link href="https://fonts.googleapis.com/css2?family=Marcellus&family=Montserrat:wght@400;500&display=swap" rel="stylesheet">
<style>
  :root {
    --backdrop: #f3e6e6;
    --espresso: #332626;
    --espresso-deep: #1e1718;
    --ivory: #ffffff;
    --mist: #e6e7e8;
  }
  * { margin: 0; padding: 0; box-sizing: border-box; }
  html, body { width: 1200px; height: 840px; overflow: hidden; }
  body {
    background: var(--backdrop);
    position: relative;
    font-family: "Montserrat", sans-serif;
  }
  .label {
    position: absolute;
    overflow: hidden;
    background: var(--espresso);
    color: var(--ivory);
  }
  .label--wide-dark { left: 97px; top: 54px; width: 529px; height: 311px; }
  .label--wide-light {
    left: 97px; top: 476px; width: 529px; height: 311px;
    background: var(--ivory); color: var(--espresso);
    border: 1px solid var(--espresso);
  }
  .label--tall { left: 719px; top: 54px; width: 384px; height: 733px; }

  .label > * { position: absolute; }
  .brand-title {
    font-family: "Marcellus", serif;
    font-weight: 400;
    font-size: 34px;
    letter-spacing: 0.3px;
    line-height: 1;
    white-space: nowrap;
  }
  .rule { height: 1px; background: currentColor; }
  .line-name, .product, .meta {
    font-size: 17px;
    font-weight: 400;
    letter-spacing: 0.6px;
    line-height: 1;
    white-space: nowrap;
  }
  .line-name sub { font-size: 9px; vertical-align: -4px; }
  .wordmark {
    display: flex; align-items: center; gap: 9px;
    font-size: 16px; font-weight: 500; letter-spacing: 0.6px; line-height: 1;
    white-space: nowrap;
  }
  .wordmark-dot { width: 32px; height: 32px; border-radius: 50%; background: currentColor; }
  .backdrop-mark { border-radius: 50%; background: var(--espresso-deep); }
  .label--wide-light .backdrop-mark { background: var(--mist); }

  /* wide labels */
  .label--wide-dark .brand-title, .label--wide-light .brand-title { left: 13px; top: 25px; }
  .label--wide-dark .rule--top, .label--wide-light .rule--top { left: 13px; width: 501px; top: 59px; }
  .label--wide-dark .line-name, .label--wide-light .line-name { left: 13px; top: 72px; }
  .label--wide-dark .wordmark, .label--wide-light .wordmark { left: 16px; top: 152px; }
  .label--wide-dark .product--en, .label--wide-light .product--en { left: 13px; top: 213px; }
  .label--wide-dark .product--fr, .label--wide-light .product--fr { left: 13px; top: 241px; }
  .label--wide-dark .rule--bottom, .label--wide-light .rule--bottom { left: 13px; width: 501px; top: 269px; }
  .label--wide-dark .meta--volume, .label--wide-light .meta--volume { left: 17px; top: 283px; }
  .label--wide-dark .meta--claim, .label--wide-light .meta--claim { right: 18px; top: 283px; }
  .label--wide-dark .backdrop-mark, .label--wide-light .backdrop-mark { left: 334px; top: 92px; width: 158px; height: 158px; }

  /* tall label */
  .label--tall .brand-title { left: 22px; top: 39px; }
  .label--tall .rule--top { left: 22px; width: 318px; top: 73px; }
  .label--tall .line-name { left: 22px; top: 86px; }
  .label--tall .backdrop-mark { left: 200px; top: 280px; width: 270px; height: 270px; }
  .label--tall .wordmark { left: 18px; top: 520px; }
  .label--tall .product--en { left: 14px; top: 583px; }
  .label--tall .product--fr { left: 14px; top: 611px; }
  .label--tall .rule--mid { left: 14px; width: 331px; top: 640px; }
  .label--tall .meta--volume { left: 18px; top: 652px; }
  .label--tall .rule--bottom { left: 14px; width: 331px; top: 683px; }
  .label--tall .meta--claim { left: 14px; top: 699px; }
</style>
</head>
<body>

<section class="label label--wide-dark">
  <h1 class="brand-title">VERDANT CREST MD</h1>
  <div class="rule rule--top"></div>
  <p class="line-name">VC<sub>x</sub> for Men</p>
  <div class="backdrop-mark" role="img" aria-label="Faint brand emblem area"></div>
  <div class="wordmark"><span class="wordmark-dot"></span>Verdant Crest</div>
  <p class="product product--en">Lightweight Moisturizer</p>
  <p class="product product--fr">Soin Hydratant Fluide</p>
  <div class="rule rule--bottom"></div>
  <p class="meta meta--volume">e59ml / 2fl oz</p>
  <p class="meta meta--claim">Supplement is Doctor Approved</p>
</section>

<section class="label label--wide-light">
  <h1 class="brand-title">VERDANT CREST MD</h1>
  <div class="rule rule--top"></div>
  <p class="line-name">VC<sub>x</sub> for Men</p>
  <div class="backdrop-mark" role="img" aria-label="Faint brand emblem area"></div>
  <div class="wordmark"><span class="wordmark-dot"></span>Verdant Crest</div>
  <p class="product product--en">Lightweight Moisturizer</p>
  <p class="product product--fr">Soin Hydratant Fluide</p>
  <div class="rule rule--bottom"></div>
  <p class="meta meta--volume">e59ml / 2fl oz</p>
  <p class="meta meta--claim">Supplement is Doctor Approved</p>
</section>

<section class="label label--tall">
  <h1 class="brand-title">VERDANT CREST MD</h1>
  <div class="rule rule--top"></div>
  <p class="line-name">VC<sub>x</sub> for Men</p>
  <div class="backdrop-mark" role="img" aria-label="Faint brand emblem area"></div>
  <div class="wordmark"><span class="wordmark-dot"></span>Verdant Crest</div>
  <p class="product product--en">Lightweight Moisturizer</p>
  <p class="product product--fr">Soin Hydratant Fluide</p>
  <div class="rule rule--mid"></div>
  <p class="meta meta--volume">e59ml / 2fl oz</p>
  <div class="rule rule--bottom"></div>
  <p class="meta meta--claim">Supplement is Doctor Approved</p>
</section>

</body>
</html>
```